Visitenkarten-Design für Bewertung von Grundstücken
Zielgruppe
Ich bin Sachverständige für die Bewertung von bebauten und unbebauten Grundstücken und erstelle Verkehrswertgutachten für (überwiegend) Sylter Immobilien. Meine Zielgruppe sind die Eigentümer dieser Immobilien, die aus verschiedensten Gründen eine Wertermittlung für ihre Immobilie benötigen, z.B. wegen
steuerlichen Anlässen (Erbschaft, Übertragung, Schenkung)
Erbauseinandersetzungen / Pflichtteilsansprüchen
Ehescheidung
Kauf oder Verkauf eines Grundstücks
Vermögensaufstellung
Vormundschaftsangelegenheiten
Bewertung von Rechten und Belastungen (Wohnrecht, Nießbrauch, Erbbaurecht)
Aufgabenstellung
Ich habe mir erst kürzlich eine kleine Homepage erstellen lassen, die mir sehr gut gefällt.
www.wertgutachten-haldorf.de
Das Design der Visitenkarte sollte dazu passen und prägnant und schnörkellos sein. Mein Logo mit der Lupe sollte sich dort wiederfinden, ebenfalls die Farben. Ich bevorzuge schlichte Eleganz, eine schöne Haptik, hochwertiges Papier, evtl mit Prägedruck, da bin ich aber noch unsicher, evtl. eine matte und eine Hochglanzseite....

```html
<!DOCTYPE html>
<html lang="de">
<head>
<meta charset="utf-8">
<title>Visitenkarte – Sachverständigenbüro Haldorf</title>
<link rel="stylesheet" href="https://fonts.googleapis.com/css2?family=Open+Sans:wght@400;600;700&display=swap">
<style>
  :root {
    --stage: #3b3c40;
    --card-light: #ffffff;
    --card-dark: #272b36;
    --ink: #1f1f22;
    --ink-soft: #3c3c40;
    --accent: #8fc27a;
    --on-dark: #d9dadd;
  }
  * { box-sizing: border-box; margin: 0; padding: 0; }
  html, body { width: 1200px; height: 977px; overflow: hidden; }
  body {
    background: var(--stage);
    font-family: "Open Sans", Arial, sans-serif;
    position: relative;
  }
  .card {
    position: absolute;
    top: 320px;
    width: 520px;
    height: 337px;
    border-radius: 22px;
    overflow: hidden;
  }
  .card--front { left: 50px; background: var(--card-light); }
  .card--back  { left: 630px; background: var(--card-dark); }

  .brand {
    position: absolute;
    left: 34px; top: 42px;
    display: flex; align-items: center; gap: 8px;
    white-space: nowrap;
  }
  .brand__dot {
    width: 16px; height: 16px; border-radius: 50%;
    background: var(--ink);
    flex: none;
  }
  .brand__name {
    font-weight: 700;
    font-size: 15px;
    letter-spacing: 0.4px;
    text-transform: uppercase;
    color: var(--ink);
  }
  .brand__owner {
    position: absolute;
    left: 58px; top: 66px;
    font-weight: 600;
    font-size: 13px;
    letter-spacing: 0.6px;
    text-transform: uppercase;
    color: var(--accent);
    white-space: nowrap;
  }
  .person {
    position: absolute;
    right: 56px; top: 132px;
    text-align: right;
    white-space: nowrap;
  }
  .person__name {
    font-weight: 700;
    font-size: 21px;
    letter-spacing: 0.5px;
    color: var(--ink);
    text-transform: uppercase;
  }
  .person__role {
    font-size: 14px;
    color: var(--ink-soft);
    margin-top: -2px;
  }
  .accent-bar {
    position: absolute;
    right: 26px; top: 140px;
    width: 18px; height: 38px;
    background: var(--accent);
  }
  .contact {
    position: absolute;
    right: 26px; bottom: 40px;
    list-style: none;
    text-align: right;
  }
  .contact li {
    display: flex; justify-content: flex-end; align-items: center; gap: 10px;
    font-size: 14px;
    line-height: 22px;
    color: var(--ink);
    white-space: nowrap;
  }
  .contact svg { width: 13px; height: 13px; fill: var(--accent); flex: none; }

  .card--back .brand { left: 0; right: 0; top: 132px; justify-content: center; }
  .card--back .brand__dot { background: var(--on-dark); }
  .card--back .brand__name { color: var(--on-dark); font-size: 18px; }
  .card--back .brand__owner { left: 0; right: 0; top: 164px; text-align: center; font-size: 15px; }
</style>
</head>
<body>
  <section class="card card--front" aria-label="Vorderseite">
    <div class="brand">
      <span class="brand__dot"></span>
      <span class="brand__name">Sachverständigenbüro Haldorf</span>
    </div>
    <div class="brand__owner">Greta Haldorf</div>

    <div class="person">
      <p class="person__name">Exemple Name</p>
      <p class="person__role">Director</p>
    </div>
    <div class="accent-bar"></div>

    <ul class="contact">
      <li>0461 55230-10
        <svg viewBox="0 0 16 16"><path d="M3.6 1.2l2.2 2.6-1.3 1.6c.9 2 2.4 3.5 4.3 4.4l1.6-1.3 2.6 2.2-1.4 2.6C6.8 13 3 9.2 1 4.3z"/></svg>
      </li>
      <li>beispiel-mail@postfach.de
        <svg viewBox="0 0 16 16"><path d="M1 3h14v10H1z M2.5 4.5L8 8.8l5.5-4.3v-.2h-11z" fill-rule="evenodd"/></svg>
      </li>
      <li>Dünenweg 14B, Haldorf
        <svg viewBox="0 0 16 16"><path d="M8 1a5 5 0 0 0-5 5c0 3.6 5 9 5 9s5-5.4 5-9a5 5 0 0 0-5-5zm0 7a2 2 0 1 1 0-4 2 2 0 0 1 0 4z"/></svg>
      </li>
    </ul>
  </section>

  <section class="card card--back" aria-label="Rückseite">
    <div class="brand">
      <span class="brand__dot"></span>
      <span class="brand__name">Sachverständigenbüro Haldorf</span>
    </div>
    <div class="brand__owner">Greta Haldorf</div>
  </section>
</body>
</html>
```